you will use Ai to Copy the website Wanderbay.com to come up with the basic frame work and it will give you the understanding of how I would like Coachlend.com to be like. Coachlend.com is a peer to peer rv rental site very similar to both of the other rv rental sites the difference is that are commission based 20% and above per rental and we will be one flat monthly rate and they keep all the earnings. Below is photo that will help you with the color scheme and the look and feel of the design

1 page

```html
<!DOCTYPE html>
<html lang="en">
<head>
<meta charset="utf-8">
<title>Coachlend — The Smarter Way to Rent &amp; Own RVs</title>
<link href="https://fonts.googleapis.com/css2?family=Libre+Caslon+Text:wght@400;700&family=Poppins:wght@400;500;600;700&display=swap" rel="stylesheet">
<style>
:root{
  --navy:#0c1733;
  --navy-2:#1b2b4d;
  --green:#5f9128;
  --green-2:#7fb536;
  --ink:#1a1a1a;
  --muted:#6b6b6b;
  --line:#d9d9d9;
  --soft:#f2f2f2;
  --white:#ffffff;
}
*{box-sizing:border-box;margin:0;padding:0}
html,body{width:1200px;height:5372px;overflow:hidden;background:var(--white)}
body{position:relative;font-family:'Poppins',sans-serif;color:var(--ink)}
.abs{position:absolute}
.serif{font-family:'Libre Caslon Text',serif;text-transform:uppercase;font-weight:400;letter-spacing:.5px}

.logo{left:121px;top:42px;font-family:'Libre Caslon Text',serif;font-size:17px;letter-spacing:.5px}
.btn-host{left:824px;top:31px;width:148px;height:40px;border-radius:20px;background:var(--navy);color:#fff;font-size:12px;font-weight:500;display:flex;align-items:center;justify-content:center}
.icon-btn{top:31px;width:40px;height:40px;border-radius:50%;border:1.5px solid #999;display:flex;align-items:center;justify-content:center}

.hero-title{left:0;width:1200px;top:130px;text-align:center;font-size:35px}
.hero-sub{left:0;width:1200px;top:190px;text-align:center;font-size:25px;font-weight:500;line-height:36px}
.hero-photo{left:17px;top:261px;width:1166px;height:626px;border-radius:0 0 50px 50px;
  background:linear-gradient(180deg,#fff 0%,#dfe6ea 10%,#a9b4b7 30%,#8a7448 55%,#3d4a46 75%,#6d6a60 100%)}
.search{left:104px;top:317px;width:990px;height:71px;background:#fff;border-radius:36px;box-shadow:0 4px 18px rgba(0,0,0,.12);display:flex;align-items:center}
.search .field{height:71px;border-right:1px solid #e3e3e3;padding:14px 22px 0;font-size:11px}
.search .field small{display:block;color:#888;font-size:11px;margin-bottom:4px}
.search .field b{font-weight:500}
.search .go{margin-left:auto;margin-right:14px;width:46px;height:46px;border-radius:50%;background:var(--navy);display:flex;align-items:center;justify-content:center}

.h2{font-size:31px}
.lead{font-size:13px;font-weight:500}

.chips{display:flex;gap:10px}
.chip{height:40px;border-radius:20px;border:1.5px solid #cfcfcf;padding:0 22px;display:flex;align-items:center;gap:8px;font-size:13px;font-weight:500;color:#333}
.chip.on{background:var(--green);border-color:var(--green);color:#fff}

.rcard{top:1252px;width:305px}
.rcard .photo{height:205px;border-radius:10px;position:relative}
.pin-tag{position:absolute;left:22px;bottom:-10px;height:42px;padding:0 22px;border-radius:21px;background:var(--navy);color:#fff;font-size:12px;font-weight:500;display:flex;align-items:center;gap:8px}
.heart{position:absolute;right:12px;top:16px;width:36px;height:36px;border-radius:50%;background:#fff;display:flex;align-items:center;justify-content:center}
.rcard .title{margin-top:34px;display:flex;justify-content:space-between;align-items:center;font-size:16px;font-weight:600}
.rcard .title span{font-size:12px;color:var(--green);font-weight:500}
.rcard .meta{margin-top:22px;display:flex;justify-content:space-between;font-size:12px;color:#444}
.rcard .meta div{display:flex;align-items:center;gap:6px}
.rcard .price{margin-top:18px;display:flex;align-items:center;font-size:12px;color:#444}
.rcard .price small{margin-left:auto;color:var(--green);font-size:10px;margin-right:6px}
.rcard .price b{font-size:18px;font-weight:600;color:var(--ink)}
.outline-btn{height:38px;border-radius:19px;border:1.5px solid #888;display:flex;align-items:center;justify-content:center;font-size:12px;font-weight:600}

.why{left:17px;top:1805px;width:1166px;height:868px;border-radius:8px;background:linear-gradient(135deg,var(--navy-2) 0%,var(--navy) 45%,#0a1226 100%);color:#fff}
.why .c{position:absolute;left:0;width:1166px;text-align:center}
.hl{color:var(--green-2)}
.compare-btn{position:absolute;top:347px;height:54px;border-radius:27px;display:flex;align-items:center;padding-left:22px;font-size:18px;font-weight:600}
.list{position:absolute;top:447px;list-style:none;font-size:12px}
.list li{display:flex;align-items:center;gap:14px;height:46px}

.acard{top:2943px;width:305px}
.acard .photo{height:205px;position:relative}
.acard .row{margin-top:22px;display:flex;justify-content:space-between;align-items:flex-start}
.acard .row b{font-size:17px;font-weight:600;margin-top:14px}
.acard .row small{font-size:10px;color:var(--green);line-height:20px;margin-right:18px}
.arrow{top:2793px;width:30px;height:30px;border-radius:50%;border:1.5px solid #333;display:flex;align-items:center;justify-content:center}

.faq{left:152px;top:3346px;width:896px;height:607px;background:var(--soft);border-radius:6px}
.faq-row{position:absolute;left:151px;width:605px;height:64px;border-bottom:1.5px solid #cfcfcf;display:flex;align-items:center;justify-content:space-between;padding:0 16px;font-size:14px;font-weight:500}

.cities{left:104px;top:4304px;width:966px;height:160px;overflow:hidden}
.city{position:absolute;width:170px}
.city .n{display:flex;align-items:center;gap:10px;font-size:13px;font-weight:500;white-space:nowrap}
.city .c{font-size:12px;color:var(--green);margin-top:6px;white-space:nowrap}

.cta{left:17px;top:4556px;width:1166px;height:422px;border-radius:8px;background:linear-gradient(90deg,#4f7f1d 0%,#679c2a 60%,#84b938 100%);color:#fff;text-align:center}
.cta-btn{position:absolute;top:303px;height:38px;border-radius:19px;font-size:12px;font-weight:500;display:flex;align-items:center;justify-content:center}

.fcol{top:5032px;font-size:11px}
.fcol h4{font-weight:400;color:var(--green);font-size:12px;margin-bottom:14px}
.fcol li{list-style:none;line-height:19px}
.fcol li::before{content:"• ";}
.bigline{left:0;top:5178px;white-space:nowrap;font-size:84px;font-weight:700;color:#e4e4e4;letter-spacing:1px}
.copy{left:0;width:1200px;top:5305px;text-align:center;font-size:12px}
</style>
</head>
<body>

<div class="abs logo">COACHLEND</div>
<div class="abs btn-host">Become a Host</div>
<div class="abs icon-btn" style="left:985px"><svg width="20" height="14" viewBox="0 0 20 14"><path d="M1 1h18M1 7h18M1 13h18" stroke="#111" stroke-width="2"/></svg></div>
<div class="abs icon-btn" style="left:1038px"><svg width="16" height="18" viewBox="0 0 16 18"><circle cx="8" cy="5" r="4" fill="none" stroke="#111" stroke-width="1.5"/><path d="M1 17c0-4 3-6 7-6s7 2 7 6" fill="none" stroke="#111" stroke-width="1.5"/></svg></div>

<h1 class="abs serif hero-title">The Smarter Way to Rent &amp; Own RVs</h1>
<p class="abs hero-sub">Keep 100% Of Every Rental. Pay One<br>Simple Monthly Fee.</p>
<div class="abs hero-photo" role="img" aria-label="Motorhome parked on a lakeshore with autumn trees and snowy mountains reflected in the water"></div>
<div class="abs search">
  <div class="field" style="width:232px;padding-top:26px;color:#888;padding-left:36px">Locations</div>
  <div class="field" style="width:154px"><small>Dates</small><b>Any Dates</b></div>
  <div class="field" style="width:154px"><small>Guests</small><b>2 Guests</b></div>
  <div class="field" style="width:154px"><small>Drivers Age</small><b>25 +</b></div>
  <div class="field" style="width:200px;border:none"><small>Rent Type</small><b>All Type</b></div>
  <div class="go"><svg width="18" height="18" viewBox="0 0 18 18"><circle cx="8" cy="8" r="6" fill="none" stroke="#fff" stroke-width="1.6"/><path d="M12.5 12.5 17 17" stroke="#fff" stroke-width="1.6"/></svg></div>
</div>

<h2 class="abs serif h2" style="left:121px;top:1018px">Find the Best RV Rentals</h2>
<p class="abs lead" style="left:121px;top:1103px">Choose To Drive It Yourself Or Have It Delivered And Completely Set Up At Your Destination.</p>
<div class="abs chips" style="left:121px;top:1166px">
  <div class="chip on"><svg width="16" height="14" viewBox="0 0 16 14"><path d="M8 13 1.5 6.5A3.5 3.5 0 0 1 8 2a3.5 3.5 0 0 1 6.5 4.5Z" fill="none" stroke="#fff" stroke-width="1.4"/></svg>Popular</div>
  <div class="chip"><svg width="18" height="12" viewBox="0 0 18 12"><rect x="1" y="1" width="16" height="8" rx="2" fill="none" stroke="#777" stroke-width="1.3"/></svg>Camper Van</div>
  <div class="chip"><svg width="18" height="12" viewBox="0 0 18 12"><rect x="1" y="1" width="16" height="8" rx="3" fill="none" stroke="#777" stroke-width="1.3"/></svg>Vintage</div>
  <div class="chip"><svg width="18" height="12" viewBox="0 0 18 12"><rect x="1" y="1" width="13" height="8" rx="2" fill="none" stroke="#777" stroke-width="1.3"/><path d="M14 7h3" stroke="#777"/></svg>Small Trailer</div>
  <div class="chip"><svg width="14" height="14" viewBox="0 0 14 14"><circle cx="7" cy="8" r="4" fill="none" stroke="#777" stroke-width="1.3"/></svg>Pets</div>
  <div class="chip"><svg width="14" height="14" viewBox="0 0 14 14"><path d="M2 5h10L7 13Z" fill="none" stroke="#777" stroke-width="1.3"/></svg>Value</div>
</div>

<div class="abs rcard" style="left:106px">
  <div class="photo" role="img" aria-label="White motorhome on a road before dramatic mountains" style="background:linear-gradient(180deg,#5b6670,#9aa3a6 50%,#4a4f4a)">
    <div class="heart"><svg width="16" height="14" viewBox="0 0 16 14"><path d="M8 13 1.5 6.5A3.5 3.5 0 0 1 8 2a3.5 3.5 0 0 1 6.5 4.5Z" fill="none" stroke="#111" stroke-width="1.4"/></svg></div>
    <div class="pin-tag"><svg width="12" height="15" viewBox="0 0 12 15"><path d="M6 14s5-5 5-8.5A5 5 0 0 0 1 5.5C1 9 6 14 6 14Z" fill="none" stroke="#fff" stroke-width="1.3"/><circle cx="6" cy="5.5" r="1.8" fill="none" stroke="#fff"/></svg>Las Vegas, NV</div>
  </div>
  <div class="title">Freedom Hauler <span>★ 5.0 (5)</span></div>
  <div class="meta"><div><svg width="26" height="16" viewBox="0 0 26 16"><rect x="1" y="2" width="22" height="10" rx="2" fill="none" stroke="#555" stroke-width="1.3"/></svg>Premium Toy Hauler</div><div><svg width="22" height="18" viewBox="0 0 22 18"><path d="M3 16V4h16v12M3 11h16" fill="none" stroke="#555" stroke-width="1.3"/></svg>Sleeps 7</div></div>
  <div class="price"><svg width="22" height="22" viewBox="0 0 22 22" style="margin-right:8px"><rect x="1" y="1" width="20" height="20" rx="3" fill="none" stroke="#555" stroke-width="1.3"/><path d="M6 16 16 6" stroke="#555"/></svg>30 Ft<small>Starting At</small><b>$149/Night</b></div>
</div>

<div class="abs rcard" style="left:449px">
  <div class="photo" role="img" aria-label="Motorhome beside a turquoise mountain lake" style="background:linear-gradient(180deg,#b7c4cc,#7e9aa0 50%,#3f7a78)">
    <div class="heart"><svg width="16" height="14" viewBox="0 0 16 14"><path d="M8 13 1.5 6.5A3.5 3.5 0 0 1 8 2a3.5 3.5 0 0 1 6.5 4.5Z" fill="none" stroke="#111" stroke-width="1.4"/></svg></div>
    <div class="pin-tag"><svg width="12" height="15" viewBox="0 0 12 15"><path d="M6 14s5-5 5-8.5A5 5 0 0 0 1 5.5C1 9 6 14 6 14Z" fill="none" stroke="#fff" stroke-width="1.3"/><circle cx="6" cy="5.5" r="1.8" fill="none" stroke="#fff"/></svg>Las Vegas, NV</div>
  </div>
  <div class="title">Freedom Hauler <span>★ 5.0 (5)</span></div>
  <div class="meta"><div><svg width="26" height="16" viewBox="0 0 26 16"><rect x="1" y="2" width="22" height="10" rx="2" fill="none" stroke="#555" stroke-width="1.3"/></svg>Premium Toy Hauler</div><div><svg width="22" height="18" viewBox="0 0 22 18"><path d="M3 16V4h16v12M3 11h16" fill="none" stroke="#555" stroke-width="1.3"/></svg>Sleeps 7</div></div>
  <div class="price"><svg width="22" height="22" viewBox="0 0 22 22" style="margin-right:8px"><rect x="1" y="1" width="20" height="20" rx="3" fill="none" stroke="#555" stroke-width="1.3"/><path d="M6 16 16 6" stroke="#555"/></svg>30 Ft<small>Starting At</small><b>$149/Night</b></div>
</div>

<div class="abs rcard" style="left:791px">
  <div class="photo" role="img" aria-label="Travel trailer at a forest campsite with picnic table" style="background:linear-gradient(180deg,#4f6a55,#7b8a78 50%,#3a4a36)">
    <div class="heart"><svg width="16" height="14" viewBox="0 0 16 14"><path d="M8 13 1.5 6.5A3.5 3.5 0 0 1 8 2a3.5 3.5 0 0 1 6.5 4.5Z" fill="none" stroke="#111" stroke-width="1.4"/></svg></div>
    <div class="pin-tag"><svg width="12" height="15" viewBox="0 0 12 15"><path d="M6 14s5-5 5-8.5A5 5 0 0 0 1 5.5C1 9 6 14 6 14Z" fill="none" stroke="#fff" stroke-width="1.3"/><circle cx="6" cy="5.5" r="1.8" fill="none" stroke="#fff"/></svg>Las Vegas, NV</div>
  </div>
  <div class="title">Freedom Hauler <span>★ 5.0 (5)</span></div>
  <div class="meta"><div><svg width="26" height="16" viewBox="0 0 26 16"><rect x="1" y="2" width="22" height="10" rx="2" fill="none" stroke="#555" stroke-width="1.3"/></svg>Premium Toy Hauler</div><div><svg width="22" height="18" viewBox="0 0 22 18"><path d="M3 16V4h16v12M3 11h16" fill="none" stroke="#555" stroke-width="1.3"/></svg>Sleeps 7</div></div>
  <div class="price"><svg width="22" height="22" viewBox="0 0 22 22" style="margin-right:8px"><rect x="1" y="1" width="20" height="20" rx="3" fill="none" stroke="#555" stroke-width="1.3"/><path d="M6 16 16 6" stroke="#555"/></svg>30 Ft<small>Starting At</small><b>$149/Night</b></div>
</div>

<div class="abs outline-btn" style="left:515px;top:1667px;width:170px">Explore All Rentals</div>

<section class="abs why">
  <h2 class="c serif" style="top:86px;font-size:29px">Why Coachlend?</h2>
  <p class="c" style="top:178px;font-size:13px;line-height:26px">Unlike Other RV Rental Marketplaces That Take <span class="hl">20% Or More From Every Booking</span>, Coachlend Lets Owners Pay One Affordable<br>Monthly Subscription And <span class="hl">Keep 100% Of Every Rental Dollar They Earn.</span></p>
  <p class="c" style="top:255px;font-size:13px">Whether You Rent Your RV Once A Month Or Every Weekend, Your Profits Stay Where They Belong—With You.</p>
  <div class="compare-btn" style="left:242px;width:315px;background:#fff;color:var(--ink)">Traditional Rental Platforms</div>
  <div class="compare-btn" style="left:626px;width:313px;background:var(--green)">Coachlend</div>
  <div style="position:absolute;left:590px;top:340px;width:1px;height:307px;background:#fff"></div>
  <ul class="list" style="left:281px">
    <li><svg width="18" height="18" viewBox="0 0 18 18"><circle cx="9" cy="9" r="7.5" fill="none" stroke="#fff" stroke-width="1.2"/><path d="m5.5 9 2.5 2.5 4.5-5" fill="none" stroke="#fff" stroke-width="1.2"/></svg>20%+ Commission Per Booking</li>
    <li><svg width="18" height="18" viewBox="0 0 18 18"><circle cx="9" cy="9" r="7.5" fill="none" stroke="#fff" stroke-width="1.2"/><path d="m5.5 9 2.5 2.5 4.5-5" fill="none" stroke="#fff" stroke-width="1.2"/></svg>Earnings Reduced Every Rental</li>
    <li><svg width="18" height="18" viewBox="0 0 18 18"><circle cx="9" cy="9" r="7.5" fill="none" stroke="#fff" stroke-width="1.2"/><path d="m5.5 9 2.5 2.5 4.5-5" fill="none" stroke="#fff" stroke-width="1.2"/></svg>Fees Increase As You Earn More</li>
    <li><svg width="18" height="18" viewBox="0 0 18 18"><circle cx="9" cy="9" r="7.5" fill="none" stroke="#fff" stroke-width="1.2"/><path d="m5.5 9 2.5 2.5 4.5-5" fill="none" stroke="#fff" stroke-width="1.2"/></svg>Less Control Over Profits</li>
  </ul>
  <ul class="list" style="left:665px">
    <li><svg width="18" height="18" viewBox="0 0 18 18"><circle cx="9" cy="9" r="7.5" fill="none" stroke="#7fb536" stroke-width="1.2"/><path d="m5.5 9 2.5 2.5 4.5-5" fill="none" stroke="#7fb536" stroke-width="1.2"/></svg>Flat Monthly Membership</li>
    <li><svg width="18" height="18" viewBox="0 0 18 18"><circle cx="9" cy="9" r="7.5" fill="none" stroke="#7fb536" stroke-width="1.2"/><path d="m5.5 9 2.5 2.5 4.5-5" fill="none" stroke="#7fb536" stroke-width="1.2"/></svg>Keep 100% Of Rental Income</li>
    <li><svg width="18" height="18" viewBox="0 0 18 18"><circle cx="9" cy="9" r="7.5" fill="none" stroke="#7fb536" stroke-width="1.2"/><path d="m5.5 9 2.5 2.5 4.5-5" fill="none" stroke="#7fb536" stroke-width="1.2"/></svg>Predictable Monthly Cost</li>
    <li><svg width="18" height="18" viewBox="0 0 18 18"><circle cx="9" cy="9" r="7.5" fill="none" stroke="#7fb536" stroke-width="1.2"/><path d="m5.5 9 2.5 2.5 4.5-5" fill="none" stroke="#7fb536" stroke-width="1.2"/></svg>Unlimited Earning Potential</li>
  </ul>
  <p class="c serif" style="top:720px;font-size:16px;line-height:31px">Why Give Away Hundreds - Or Even Thousands - In Commissions Every Year<br>When You Can Keep Every Dollar You Earn?</p>
</section>

<h2 class="abs serif h2" style="left:121px;top:2795px">Find Your Next RV Adventure</h2>
<div class="abs arrow" style="left:1018px"><svg width="10" height="10" viewBox="0 0 10 10"><path d="M7 1 3 5l4 4" fill="none" stroke="#333" stroke-width="1.5"/></svg></div>
<div class="abs arrow" style="left:1058px;border-color:var(--green)"><svg width="10" height="10" viewBox="0 0 10 10"><path d="m3 1 4 4-4 4" fill="none" stroke="#5f9128" stroke-width="1.5"/></svg></div>
<p class="abs lead" style="left:121px;top:2881px">Explore Premium RVs Across The Country And Start Your Next Unforgettable Road Trip. From $45/Night.</p>

<div class="abs acard" style="left:104px">
  <div class="photo" role="img" aria-label="Aerial view of a white sand beach with turquoise water" style="background:linear-gradient(180deg,#9fd4f0,#3fb9c9 45%,#e9e2cf 80%,#cfc6b0)">
    <div class="pin-tag"><svg width="12" height="15" viewBox="0 0 12 15"><path d="M6 14s5-5 5-8.5A5 5 0 0 0 1 5.5C1 9 6 14 6 14Z" fill="none" stroke="#fff" stroke-width="1.3"/><circle cx="6" cy="5.5" r="1.8" fill="none" stroke="#fff"/></svg>Florida</div>
  </div>
  <div class="row"><b>Beach Escapes</b><small>▬ +285 RVs<br>Available</small></div>
</div>
<div class="abs acard" style="left:445px">
  <div class="photo" role="img" aria-label="Camper van parked on a mountain ridge at sunset" style="background:linear-gradient(180deg,#a98f78,#7c6f66 45%,#4a4642)">
    <div class="pin-tag"><svg width="12" height="15" viewBox="0 0 12 15"><path d="M6 14s5-5 5-8.5A5 5 0 0 0 1 5.5C1 9 6 14 6 14Z" fill="none" stroke="#fff" stroke-width="1.3"/><circle cx="6" cy="5.5" r="1.8" fill="none" stroke="#fff"/></svg>Colorado</div>
  </div>
  <div class="row"><b>Mountain Adventures</b><small>▬ +285 RVs<br>Available</small></div>
</div>
<div class="abs acard" style="left:785px">
  <div class="photo" role="img" aria-label="Tent glowing at a lakeside forest campsite" style="background:linear-gradient(180deg,#6c6a4e,#4b5338 50%,#2c3226)">
    <div class="pin-tag"><svg width="12" height="15" viewBox="0 0 12 15"><path d="M6 14s5-5 5-8.5A5 5 0 0 0 1 5.5C1 9 6 14 6 14Z" fill="none" stroke="#fff" stroke-width="1.3"/><circle cx="6" cy="5.5" r="1.8" fill="none" stroke="#fff"/></svg>Michigan</div>
  </div>
  <div class="row"><b>Lakeside Camping</b><small>▬ +285 RVs<br>Available</small></div>
</div>

<section class="abs faq">
  <h2 class="serif" style="position:absolute;left:0;width:896px;top:96px;text-align:center;font-size:31px">Frequently Asked Questions</h2>
  <div style="position:absolute;left:390px;top:152px;width:116px;height:3px;background:var(--green)"></div>
  <div class="faq-row" style="top:195px">HOW IS COACHLEND DIFFERENT?<svg width="18" height="18" viewBox="0 0 18 18"><path d="M9 1v16M1 9h16" stroke="#333" stroke-width="1.4"/></svg></div>
  <div class="faq-row" style="top:259px">WHO CAN LIST AN RV?<svg width="18" height="18" viewBox="0 0 18 18"><path d="M9 1v16M1 9h16" stroke="#333" stroke-width="1.4"/></svg></div>
  <div class="faq-row" style="top:323px">WHAT TYPES OF RVS CAN I RENT?<svg width="18" height="18" viewBox="0 0 18 18"><path d="M9 1v16M1 9h16" stroke="#333" stroke-width="1.4"/></svg></div>
  <div class="faq-row" style="top:387px">IS BOOKING SECURE?<svg width="18" height="18" viewBox="0 0 18 18"><path d="M9 1v16M1 9h16" stroke="#333" stroke-width="1.4"/></svg></div>
  <div class="outline-btn" style="position:absolute;left:380px;top:490px;width:136px">Explore More</div>
</section>

<h2 class="abs serif h2" style="left:104px;top:4074px">Explore RV Rentals Across the USA</h2>
<p class="abs lead" style="left:104px;top:4159px">Find The Perfect RV In Your Favorite Cities And States—Ready For Your Next Adventure.</p>
<div class="abs chips" style="left:104px;top:4224px">
  <div class="chip on"><svg width="16" height="14" viewBox="0 0 16 14"><path d="M8 13 1.5 6.5A3.5 3.5 0 0 1 8 2a3.5 3.5 0 0 1 6.5 4.5Z" fill="none" stroke="#fff" stroke-width="1.4"/></svg>Popular RV Rental Destinations</div>
  <div class="chip"><svg width="18" height="12" viewBox="0 0 18 12"><rect x="1" y="1" width="16" height="8" rx="2" fill="none" stroke="#777" stroke-width="1.3"/></svg>Search RVs By State</div>
</div>
<div class="abs cities">
  <div class="city" style="left:0;top:0"><div class="n"><svg width="14" height="18" viewBox="0 0 12 15"><path d="M6 14s5-5 5-8.5A5 5 0 0 0 1 5.5C1 9 6 14 6 14Z" fill="none" stroke="#333" stroke-width="1.2"/><circle cx="6" cy="5.5" r="1.8" fill="none" stroke="#333"/></svg>Atlanta, GA</div><div class="c">751 RV Rentals</div></div>
  <div class="city" style="left:178px;top:0"><div class="n"><svg width="14" height="18" viewBox="0 0 12 15"><path d="M6 14s5-5 5-8.5A5 5 0 0 0 1 5.5C1 9 6 14 6 14Z" fill="none" stroke="#333" stroke-width="1.2"/><circle cx="6" cy="5.5" r="1.8" fill="none" stroke="#333"/></svg>Austin, TX</div><div class="c">751 RV Rentals</div></div>
  <div class="city" style="left:355px;top:0"><div class="n"><svg width="14" height="18" viewBox="0 0 12 15"><path d="M6 14s5-5 5-8.5A5 5 0 0 0 1 5.5C1 9 6 14 6 14Z" fill="none" stroke="#333" stroke-width="1.2"/><circle cx="6" cy="5.5" r="1.8" fill="none" stroke="#333"/></svg>Boston, MA</div><div class="c">751 RV Rentals</div></div>
  <div class="city" style="left:533px;top:0"><div class="n"><svg width="14" height="18" viewBox="0 0 12 15"><path d="M6 14s5-5 5-8.5A5 5 0 0 0 1 5.5C1 9 6 14 6 14Z" fill="none" stroke="#333" stroke-width="1.2"/><circle cx="6" cy="5.5" r="1.8" fill="none" stroke="#333"/></svg>Chicago, IL</div><div class="c">751 RV Rentals</div></div>
  <div class="city" style="left:712px;top:0"><div class="n"><svg width="14" height="18" viewBox="0 0 12 15"><path d="M6 14s5-5 5-8.5A5 5 0 0 0 1 5.5C1 9 6 14 6 14Z" fill="none" stroke="#333" stroke-width="1.2"/><circle cx="6" cy="5.5" r="1.8" fill="none" stroke="#333"/></svg>Columbus, OH</div><div class="c">751 RV Rentals</div></div>
  <div class="city" style="left:889px;top:0"><div class="n"><svg width="14" height="18" viewBox="0 0 12 15"><path d="M6 14s5-5 5-8.5A5 5 0 0 0 1 5.5C1 9 6 14 6 14Z" fill="none" stroke="#333" stroke-width="1.2"/><circle cx="6" cy="5.5" r="1.8" fill="none" stroke="#333"/></svg>Dallas, TX</div><div class="c">751 RV Rentals</div></div>
  <div class="city" style="left:0;top:88px"><div class="n"><svg width="14" height="18" viewBox="0 0 12 15"><path d="M6 14s5-5 5-8.5A5 5 0 0 0 1 5.5C1 9 6 14 6 14Z" fill="none" stroke="#333" stroke-width="1.2"/><circle cx="6" cy="5.5" r="1.8" fill="none" stroke="#333"/></svg>Houston, TX</div><div class="c">751 RV Rentals</div></div>
  <div class="city" style="left:178px;top:88px"><div class="n"><svg width="14" height="18" viewBox="0 0 12 15"><path d="M6 14s5-5 5-8.5A5 5 0 0 0 1 5.5C1 9 6 14 6 14Z" fill="none" stroke="#333" stroke-width="1.2"/><circle cx="6" cy="5.5" r="1.8" fill="none" stroke="#333"/></svg>Kailua-Kona, HI</div><div class="c">751 RV Rentals</div></div>
  <div class="city" style="left:355px;top:88px"><div class="n"><svg width="14" height="18" viewBox="0 0 12 15"><path d="M6 14s5-5 5-8.5A5 5 0 0 0 1 5.5C1 9 6 14 6 14Z" fill="none" stroke="#333" stroke-width="1.2"/><circle cx="6" cy="5.5" r="1.8" fill="none" stroke="#333"/></svg>Kauai, HI</div><div class="c">751 RV Rentals</div></div>
  <div class="city" style="left:533px;top:88px"><div class="n"><svg width="14" height="18" viewBox="0 0 12 15"><path d="M6 14s5-5 5-8.5A5 5 0 0 0 1 5.5C1 9 6 14 6 14Z" fill="none" stroke="#333" stroke-width="1.2"/><circle cx="6" cy="5.5" r="1.8" fill="none" stroke="#333"/></svg>Las Vegas, NV</div><div class="c">751 RV Rentals</div></div>
  <div class="city" style="left:712px;top:88px"><div class="n"><svg width="14" height="18" viewBox="0 0 12 15"><path d="M6 14s5-5 5-8.5A5 5 0 0 0 1 5.5C1 9 6 14 6 14Z" fill="none" stroke="#333" stroke-width="1.2"/><circle cx="6" cy="5.5" r="1.8" fill="none" stroke="#333"/></svg>Maui, HI</div><div class="c">751 RV Rentals</div></div>
  <div class="city" style="left:889px;top:88px"><div class="n"><svg width="14" height="18" viewBox="0 0 12 15"><path d="M6 14s5-5 5-8.5A5 5 0 0 0 1 5.5C1 9 6 14 6 14Z" fill="none" stroke="#333" stroke-width="1.2"/><circle cx="6" cy="5.5" r="1.8" fill="none" stroke="#333"/></svg>Atlanta, GA</div><div class="c">751 RV Rentals</div></div>
</div>

<section class="abs cta">
  <h2 class="serif" style="position:absolute;left:0;width:1166px;top:86px;font-size:31px">Your Next Adventure Starts Here</h2>
  <p style="position:absolute;left:0;width:1166px;top:170px;font-size:13px;line-height:26px">Whether You're Looking To Explore The Open Road Or Turn Your RV Into A Reliable Source Of<br>Income, Coachlend Makes It Simple.</p>
  <p style="position:absolute;left:0;width:1166px;top:244px;font-size:19px;font-weight:500">Travel More. Earn More. Keep More.</p>
  <div class="cta-btn" style="left:427px;width:126px;background:var(--navy)">Find Your RV</div>
  <div class="cta-btn" style="left:572px;width:166px;border:1.5px solid #fff">List Your RV Today</div>
</section>

<div class="abs fcol" style="left:131px"><h4>Explore</h4><ul><li>Browse RVs</li><li>Popular Destinations</li><li>RV Categories</li><li>Road Trip Inspiration</li></ul></div>
<div class="abs fcol" style="left:426px"><h4>For Owners</h4><ul><li>List Your RV</li><li>Membership Plans</li><li>Owner Dashboard</li><li>Owner Resources</li></ul></div>
<div class="abs fcol" style="left:707px"><h4>Support</h4><ul><li>Help Center</li><li>FAQs</li><li>Contact Us</li><li>Safety &amp; Trust</li></ul></div>
<div class="abs fcol" style="left:958px"><h4>Company</h4><ul><li>About Coachlend</li><li>Blog</li><li>Careers</li><li>Terms &amp; Privacy</li></ul></div>
<div class="abs bigline">Flat Monthly Fee. 100% of Your Earnings.</div>
<p class="abs copy">Copyright@2026.All Rights Reserved</p>

</body>
</html>
```